business card stylish and chique

I'd like to have a new business card. I am a certified pilates instructor. my website is www.lumaflowstudio-example.com. Next to teaching pilates in napa valley and around the globe, I offer luxury wellness travel in Napa Valley. (plus I make art and healthy food. my instagram is @mrl_tvsk)
I'd love to have an eye catching (bold and unique) card that says in gold or embossed MRL TVSK . (but open for any creative idea)
The back should have my info:
MarlaTovisk@maildrop-example.com.
I love whimsical and think the murals at the Olvaro hotel in Miami and the Brivet prints are my dreamworld. I'd love on the back my email address and the whimsical design.

Target Market(s)

see description

Industry/Entity Type

Health And Wellness

Contact Information for Business Card

see above

Colors

Designer to choose colors to be used in the design.

Requirements
Must have
• multicolor on back, whimsical print (allowed to use, pref own design)
• probably just white (or black or other single color with MRL TVSK standing out
Nice to have
• open
Should not have
• crazy fonts

```html
<!DOCTYPE html>
<html lang="en">
<head>
<meta charset="utf-8">
<title>Marla Tovisk — Business Card</title>
<link href="https://fonts.googleapis.com/css2?family=Bebas+Neue&family=Open+Sans:wght@400;600&display=swap" rel="stylesheet">
<style>
  :root {
    --backdrop: #1b1c1f;
    --card-black: #141414;
    --emboss: #2b2b2b;
    --band: rgba(255, 255, 255, 0.9);
    --ink: #1a1a1a;
    --violet: #6a2fd6;
    --blue: #2a4fe0;
    --sky: #2fa8ee;
    --magenta: #e43ad0;
    --pink: #ff4f9a;
    --green: #5fae7a;
    --olive: #9a9a2e;
    --amber: #f0a54a;
  }
  * { box-sizing: border-box; margin: 0; padding: 0; }
  html, body {
    width: 1200px; height: 900px; overflow: hidden;
    background: var(--backdrop);
  }
  .canvas {
    position: relative; width: 1200px; height: 900px;
    display: flex; flex-direction: column; align-items: center; justify-content: center;
    gap: 36px;
  }
  .card {
    position: relative; width: 660px; height: 377px; overflow: hidden;
    box-shadow: 0 10px 30px rgba(0,0,0,0.45);
  }
  .card--front {
    background: var(--card-black);
    display: flex; align-items: center; justify-content: center;
  }
  .monogram {
    font-family: 'Bebas Neue', sans-serif;
    font-size: 104px; letter-spacing: 4px;
    color: var(--emboss);
  }
  .card--back { background: var(--violet); }
  .print {
    position: absolute; inset: 0;
    background:
      radial-gradient(ellipse 40% 30% at 20% 20%, var(--olive), transparent 70%),
      radial-gradient(ellipse 35% 30% at 75% 25%, var(--magenta), transparent 70%),
      radial-gradient(ellipse 30% 25% at 55% 15%, var(--blue), transparent 70%),
      radial-gradient(ellipse 35% 30% at 15% 80%, var(--blue), transparent 70%),
      radial-gradient(ellipse 35% 30% at 45% 85%, var(--sky), transparent 70%),
      radial-gradient(ellipse 30% 25% at 65% 75%, var(--amber), transparent 70%),
      radial-gradient(ellipse 30% 30% at 90% 80%, var(--green), transparent 70%),
      radial-gradient(ellipse 25% 20% at 95% 45%, var(--pink), transparent 70%),
      conic-gradient(from 30deg at 50% 50%, var(--violet), var(--blue), var(--sky), var(--green), var(--amber), var(--magenta), var(--violet));
  }
  .info-band {
    position: absolute; left: 0; right: 0; top: 148px; height: 92px;
    background: var(--band);
    display: flex; align-items: center;
    padding-left: 58px;
  }
  .name {
    font-family: 'Bebas Neue', sans-serif;
    font-size: 46px; letter-spacing: 0.5px; color: var(--ink);
    padding-right: 16px;
  }
  .divider { width: 1.5px; height: 62px; background: var(--ink); margin-right: 14px; }
  .contacts { list-style: none; font-family: 'Open Sans', sans-serif; font-size: 15.5px; color: var(--ink); line-height: 22px; }
  .contacts li { display: flex; align-items: center; gap: 9px; }
  .contacts svg { width: 13px; height: 13px; flex: none; }
</style>
</head>
<body>
<main class="canvas">
  <section class="card card--front">
    <span class="monogram">MRL TVSK</span>
  </section>

  <section class="card card--back">
    <div class="print" role="img" aria-label="Whimsical multicolour painted swirl print with paint splashes in violet, blue, magenta, green and amber"></div>
    <div class="info-band">
      <h1 class="name">Marla Tovisk</h1>
      <span class="divider"></span>
      <ul class="contacts">
        <li>
          <svg viewBox="0 0 14 14"><circle cx="7" cy="7" r="5.5" fill="none" stroke="#1a1a1a" stroke-width="1.6"/></svg>
          @mrl_tvsk
        </li>
        <li>
          <svg viewBox="0 0 14 14"><rect x="1" y="3" width="12" height="8.5" fill="none" stroke="#1a1a1a" stroke-width="1.4"/><path d="M1 3 L7 8 L13 3" fill="none" stroke="#1a1a1a" stroke-width="1.4"/></svg>
          MarlaTovisk@maildrop-example.com
        </li>
        <li>
          <svg viewBox="0 0 14 14"><circle cx="7" cy="7" r="5.8" fill="none" stroke="#1a1a1a" stroke-width="1.3"/><ellipse cx="7" cy="7" rx="2.5" ry="5.8" fill="none" stroke="#1a1a1a" stroke-width="1.1"/><line x1="1.2" y1="7" x2="12.8" y2="7" stroke="#1a1a1a" stroke-width="1.1"/></svg>
          www.lumaflowstudio-example.com
        </li>
      </ul>
    </div>
  </section>
</main>
</body>
</html>
```